Flyer Templates, Business Card & Facebook Cover Image for New Fitness Company
Flyer Templates, Business Card & Facebook Cover Image for New Fitness Company  - Sports
Creative Brief
Please note the information below as more specific guidelines: Clean, fresh, design, please avoid using any images as the ones sourced do not reflect the 'Pulse Forge / Athletic' fitness I am targeting. Text to be arranged in different sizing/ blocking. All colours to be from the logos only. Flyer 1 - Black Background Main Text 'Attention Ladies - Strong is the New Skinny' Secondary Text 'Come and Train Beyond Limits' Bullet Pointed - 'One to One Functional Assessments - Small Group Training - Fully Adaptable for Pre and Post Natal Mums' Logo in bottom right hand corner. Facebook, website, phone contact details. Flyer 2 - White Background Main Text - 1. Prevention, 2. Reversal, 3. Control Wake Up Everyday Stronger Than Yesterday Secondary Text 'Come and Train Beyond Limits' Bullet Pointed - 'One to One Functional Assessments - Small Group Training - Fully Scalable for All Levels Logo in bottom right hand corner. Facebook, website, phone contact details. Flyer 3 - Black Background Main Text 'SWEAT is Just Fat Crying' 'Train Like an Athlete. Eat Like a Caveman. Get Results' Secondary Text 'Come and Train Beyond Limits' Bullet Pointed - 'One to One Functional Assessments - Small Group Training - Body Transformation Bootcamps' Logo in bottom right hand corner. Learn More - Facebook, website, phone contact details. Flyer 4 - White Background Main Text 'Forget the Gym. The Fitness Playground has Arrived' Second Text 'FUNctional Parent and Kids After School Group Training' Bullet Pointed - Improve concentration, self esteem and strength Logo in bottom right hand corner Learn More - Facebook, website, phone contact details. Facebook Cover Image - Black Background. Logo Only with 'Train Beyond Limits' in main text next to it and contact number. Business Card Logo, 'Train Beyond Limits' text, Name, Email, Website, Phone number details
Sports
All files to be in editable format i.e. all text can be changed and edited with new text and images can be replaced. These are sample flyers - the idea is to gain a suitable template that can be modified for each marketing campaign. Facebook cover photo also need to be edit friendly.

```html
<!DOCTYPE html>
<html lang="en">
<head>
<meta charset="utf-8">
<title>Kinetic Rise Fitness – Business Card</title>
<link href="https://fonts.googleapis.com/css2?family=Arimo:wght@400;700&family=Great+Vibes&display=swap" rel="stylesheet">
<style>
  :root {
    --backdrop: #8d8d8d;
    --card-white: #ffffff;
    --brand-teal: #1a9a9c;
    --brand-orange: #ef7a2e;
    --orange-deep: #e8692a;
    --orange-light: #fde7d8;
    --ink: #3a3a3a;
    --ink-soft: #7a7a7a;
  }
  * { box-sizing: border-box; margin: 0; padding: 0; }
  html, body {
    width: 1200px; height: 901px; overflow: hidden;
    background: var(--backdrop);
    font-family: "Arimo", Arial, sans-serif;
  }
  .stage {
    position: relative; width: 1200px; height: 901px;
    display: flex; align-items: center; justify-content: center; gap: 60px;
  }
  .card {
    position: relative; width: 500px; height: 286px;
    box-shadow: 0 4px 14px rgba(0,0,0,.3);
  }
  .card-front { background: var(--card-white); }
  .card-back {
    background: radial-gradient(ellipse at center, #ffffff 0%, var(--orange-light) 35%, #f6a56e 70%, var(--orange-deep) 100%);
  }
  .brand {
    position: absolute; left: 0; right: 0;
    display: flex; flex-direction: column; align-items: center; gap: 6px;
  }
  .brand-dot {
    width: 34px; height: 34px; border-radius: 50%;
    background: var(--brand-orange);
  }
  .brand-name {
    color: var(--brand-teal); font-weight: 700; font-size: 19px; letter-spacing: .2px;
  }
  .card-front .brand { top: 34px; }
  .card-back .brand { top: 100px; }
  .tagline {
    position: absolute; left: 26px; top: 176px; width: 190px;
    font-family: "Great Vibes", cursive; font-size: 30px; line-height: 1;
    color: var(--brand-orange);
  }
  .tagline .tagline-second { display: block; margin-left: 40px; color: var(--ink-soft); }
  .contact {
    position: absolute; left: 236px; top: 180px;
    font-size: 11px; color: var(--ink);
  }
  .contact-name {
    font-size: 15px; color: var(--brand-orange); font-weight: 400; margin-bottom: 6px;
  }
  .contact-line { display: flex; align-items: center; gap: 6px; margin-top: 3px; }
  .contact-line svg { width: 10px; height: 10px; fill: var(--ink); }
  .website {
    position: absolute; left: 250px; top: 196px;
    font-size: 10px; font-weight: 700; color: var(--ink);
  }
</style>
</head>
<body>
<main class="stage">
  <section class="card card-front" aria-label="Business card front">
    <div class="brand">
      <span class="brand-dot"></span>
      <span class="brand-name">Kinetic Rise Fitness</span>
    </div>
    <p class="tagline">Train Beyond<span class="tagline-second">Limits</span></p>
    <div class="contact">
      <p class="contact-name">Daniel K. Mercer</p>
      <p class="contact-line">
        <svg viewBox="0 0 10 10"><path d="M2 0h2l1 3-1.5 1a6 6 0 0 0 2.5 2.5L7 5l3 1v2c0 1-1 2-2 2A8 8 0 0 1 0 2c0-1 1-2 2-2z"/></svg>
        1 (555) 014-2290
      </p>
      <p class="contact-line">
        <svg viewBox="0 0 10 10"><path d="M0 2h10v6H0z M0 2l5 3.5L10 2" fill="none" stroke="#3a3a3a" stroke-width="1"/></svg>
        daniel.mercer@KineticRise.com
      </p>
    </div>
  </section>

  <section class="card card-back" aria-label="Business card back">
    <div class="brand">
      <span class="brand-dot"></span>
      <span class="brand-name">Kinetic Rise Fitness</span>
    </div>
    <p class="website">www.KineticRise.com</p>
  </section>
</main>
</body>
</html>
```